Website Navigation Redesign

We are looking for a redesign of the navigation system of our website. We prefer a clean, simple, modern look.
We are looking for three elements:
1. A top level navigation that jumps between 4 subdomains: Wealth Management, Direct Indexing, Ethical Investing and Superannuation
2. A secondary navigation for each subdomain similar to the one on this page: https://parcelfolio.au/ . The elements will be (a) 3-5 menu items (b) the ability to have submenus (c) a logo (d) a login button (e) a "call-to-action" button
3. A standard footer. See the footer from https://kestrelvault.com/ for the content to be included in the footer.
Each of the sub domains have very similar logos that we also want displayed (see uploaded image)
We are looking for 1 web page version and 1 mobile version.
It will be hosted on Hubspot CMS, and so solutions that will fit easily into that solution without custom coding will be preferred.
Our typical fonts are Ubuntu and Roboto. We prefer solutions using those fonts
Thanks
Target Market(s)
Small investors
Industry/Entity Type
Financial Services
Coding
Coded - Design and coding required
Number of Pages Required
1 page

```html
<!DOCTYPE html>
<html lang="en">
<head>
<meta charset="utf-8">
<title>Parcelfolio Direct Indexing</title>
<link href="https://fonts.googleapis.com/css2?family=Roboto:wght@400;500;700&family=Roboto+Condensed:wght@400;500;700&display=swap" rel="stylesheet">
<style>
:root{
  --blue:#0d8fe8;
  --blue-dark:#0a6fc0;
  --ink:#1b1b1b;
  --text:#333;
  --muted:#666;
  --grey-bg:#f2f2f2;
  --line:#dcdcdc;
  --black:#000;
  --white:#fff;
}
*{box-sizing:border-box;margin:0;padding:0}
html,body{width:1200px;height:5232px;overflow:hidden}
body{position:relative;background:var(--white);font-family:'Roboto',sans-serif;color:var(--text)}
.abs{position:absolute}
.h-cond{font-family:'Roboto Condensed',sans-serif;font-weight:400;color:var(--ink)}
.accent{color:var(--blue);font-weight:700}
.btn{position:absolute;background:var(--blue);color:var(--white);font-size:13px;border-radius:4px;display:flex;align-items:center;justify-content:center}

/* top bar */
.topbar{left:0;top:0;width:1200px;height:56px;background:var(--black);display:flex;justify-content:center;align-items:center;gap:34px;font-size:13px;color:var(--white)}
.topbar span.active{border-bottom:2px solid var(--white);padding-bottom:3px}

/* main nav */
.mainnav{left:0;top:56px;width:1200px;height:96px;background:var(--white);border-bottom:1px solid #eee}
.logo{position:absolute;left:32px;top:24px;display:flex;align-items:center;gap:8px}
.logo .dot{width:12px;height:12px;border-radius:50%;background:var(--blue)}
.logo .name{font-family:'Roboto Condensed',sans-serif;font-weight:700;font-size:24px;color:var(--ink)}
.logo .sub{position:absolute;left:20px;top:30px;font-size:11px;color:var(--blue)}
.menu{position:absolute;left:420px;top:38px;display:flex;gap:36px;font-size:13px;color:var(--ink)}
.menu .active{border-bottom:2px solid var(--blue);padding-bottom:12px}
.nav-cta{left:975px;top:33px;width:104px;height:28px}
.nav-login{position:absolute;left:1090px;top:33px;width:80px;height:28px;border:1.5px solid var(--blue);border-radius:4px;font-size:13px;display:flex;align-items:center;justify-content:center;color:var(--ink)}

/* hero */
.hero-shape{left:0;top:152px}
.hero-title{left:24px;top:282px;font-family:'Roboto Condensed',sans-serif;font-weight:700;font-size:34px;line-height:52px;color:var(--white);letter-spacing:.5px}
.hero-title .dark{color:var(--ink);font-weight:400}
.hero-title .dark b{font-weight:700}
.hero-btn{left:36px;top:438px;width:184px;height:32px;background:#222;color:var(--white);font-size:13px;border-radius:4px;display:flex;align-items:center;justify-content:center}
.hero-art{left:660px;top:172px;width:510px;height:440px;border-radius:30px;background:radial-gradient(circle at 55% 40%,#ffcf66 0,#f6a23a 18%,#fbe9d8 40%,#ffffff 70%)}

/* custom indexes */
.ci-photo{left:97px;top:783px;width:372px;height:372px;border-radius:14px;background:linear-gradient(135deg,#3a4656,#8a98a8 45%,#222a33)}
.ci-title{left:620px;top:876px;font-size:33px}
.ci-text{left:618px;top:934px;width:470px;font-size:15px;line-height:24px;color:var(--ink)}
.ci-btn{left:618px;top:1031px;width:110px;height:32px}

/* how to */
.howto{left:0;top:1238px;width:1200px;height:940px;background:var(--grey-bg)}
.center{width:1200px;text-align:center;left:0}
.ht-title{top:1290px;font-size:33px}
.ht-sub{top:1350px;font-size:15px;line-height:25px;color:var(--ink)}
.step{width:380px}
.step .num{position:absolute;left:0;top:0;width:52px;height:52px;background:var(--black);color:var(--white);font-family:'Roboto Condensed',sans-serif;font-size:34px;font-weight:700;display:flex;align-items:center;justify-content:center}
.step .st{position:absolute;left:64px;top:-2px;font-family:'Roboto Condensed',sans-serif;font-weight:700;font-size:24px;line-height:27px;color:var(--blue)}
.step .sd{position:absolute;left:0;top:80px;font-size:15px;color:var(--ink)}
.panel{background:var(--white);overflow:hidden;font-size:11px;color:#444}
.pf-head{height:34px;background:var(--blue-dark);color:var(--white);font-weight:700;font-size:11px;padding:10px 8px}
.pf-label{margin:22px 0 0 16px}
.pf-input{margin:6px 0 0 16px;height:24px;border:1px solid #ccc;padding:4px 8px;font-size:11px}
.tile-grid{display:grid;grid-template-columns:1fr 1fr;gap:8px;padding:8px}
.tile{height:82px;border:1px solid var(--line);border-radius:6px;display:flex;flex-direction:column;align-items:center;padding-top:10px;gap:12px;font-weight:500;font-size:11px;color:#456}
.tile .ic{width:26px;height:26px;border:2.5px solid var(--blue);border-radius:50%}
.tile.on{background:var(--blue-dark);color:var(--white);border-color:var(--blue-dark)}
.tile.on .ic{border-color:var(--white);border-radius:4px}
.seize{top:2024px;font-size:33px}
.seize-btn{left:545px;top:2093px;width:110px;height:32px}

/* testimonials */
.t-title{top:2266px;font-size:33px}
.t-sub{top:2330px;font-size:15px;line-height:25px;color:var(--ink)}
.t-card{left:173px;top:2420px;width:852px;height:392px;background:var(--grey-bg);border-radius:8px}
.quote{font-family:Georgia,serif;font-size:220px;line-height:1;color:#ddd;font-weight:700}
.avatar{left:562px;top:2468px;width:74px;height:74px;border-radius:50%;background:linear-gradient(#bbb,#555);border:3px solid var(--white);box-shadow:0 0 0 1px #ccc}
.t-name{top:2578px;font-size:24px;font-weight:700;color:var(--ink)}
.t-text{left:260px;top:2642px;width:680px;font-size:15px;line-height:25px;color:var(--ink)}
.dots{left:556px;top:2758px;display:flex;gap:14px}
.dots i{width:10px;height:10px;border-radius:50%;background:#bbb}
.dots i:first-child{background:#666}

/* award */
.aw-title{top:2904px;font-size:33px}
.trophy{left:471px;top:2962px;width:276px;height:290px;border-radius:20px;background:radial-gradient(circle at 50% 35%,#ffd24d 0,#f5a623 40%,#ffffff 72%)}
.aw-text{left:265px;top:3310px;width:700px;font-size:15px;line-height:25px;color:var(--ink)}

/* recognition */
.rc-title{top:3458px;font-size:33px}
.rc-sub{top:3522px;font-size:15px;color:var(--ink)}
.rc-box{left:130px;top:3599px;width:940px;height:543px;background:var(--grey-bg)}
.rc-bar{left:130px;top:4124px;width:940px;height:18px;background:#c8c8c8}
.press{left:130px;width:454px;background:linear-gradient(180deg,#fafafa,#d8d8d8);border:1px solid #bbb}
.rc-h{left:617px;font-size:15px;font-weight:700;color:var(--ink)}
.rc-p{left:617px;width:410px;font-size:15px;line-height:25px;color:var(--ink)}
.rc-p u{color:var(--ink)}

/* cta */
.cta-photo{left:8px;top:4222px;width:1192px;height:660px;background:linear-gradient(135deg,#111 0,#3c3c3c 40%,#777 60%,#1a1a1a 100%)}
.cta-panel{left:682px;top:4578px;width:493px;height:278px;background:rgba(225,225,225,.93);border-left:4px solid var(--blue)}
.cta-title{left:722px;top:4614px;font-size:32px;line-height:50px}
.cta-text{left:722px;top:4740px;width:420px;font-size:15px;line-height:25px;color:var(--ink)}
.cta-text a{color:var(--blue);text-decoration:none}

/* footer */
.f-col{top:4922px;font-size:13px;color:#444}
.f-col h4{font-size:14px;font-weight:700;color:var(--ink);padding-bottom:8px;border-bottom:1px solid var(--line);margin-bottom:14px}
.f-col li{list-style:none;font-size:12px;line-height:26px;color:#444}
.f-disc{left:26px;top:5118px;width:640px;font-size:11px;line-height:17px;color:#555}
.f-disc u{color:var(--blue-dark)}
.f-btn{top:5122px;height:22px;font-size:11px;border-radius:3px}
.f-copy{left:1000px;top:5160px;font-size:11px;color:#555}
</style>
</head>
<body>

<div class="abs topbar">
  <span>Wealth Management</span><span class="active">Direct Indexing</span><span>Ethical Investing</span><span>Superannuation</span>
</div>

<header class="abs mainnav">
  <div class="logo"><span class="dot"></span><span class="name">Parcelfolio</span><span class="sub">Direct Indexing</span></div>
  <nav class="menu"><span class="active">Home</span><span>Investments</span><span>Blogs</span><span>About Us</span><span>Contact Us</span></nav>
  <div class="btn nav-cta">See Portfolio</div>
  <div class="nav-login">Log In</div>
</header>

<svg class="abs hero-shape" width="640" height="490" viewBox="0 0 640 490">
  <polygon points="0,0 520,0 640,175 0,490" fill="#0d8fe8"/>
</svg>
<h1 class="abs hero-title">PERSONALISED PORTFOLIOS<br><span class="dark"><b>FOR</b> ENGAGED INVESTORS</span></h1>
<div class="abs hero-btn">Personalise your portfolio</div>
<div class="abs hero-art" role="img" aria-label="Illustration of an investor carrying a large gold coin beside a potted plant"></div>

<div class="abs ci-photo" role="img" aria-label="Photo of a desktop screen showing direct indexing investment dashboards"></div>
<h2 class="abs h-cond ci-title">Custom <span class="accent">Indexes</span></h2>
<p class="abs ci-text">Tailor your superannuation and investment portfolios with Parcelfolio Direct Indexing's innovative, award winning, direct investing solution.</p>
<div class="btn ci-btn">Start Now</div>

<section class="abs howto"></section>
<h2 class="abs center h-cond ht-title">How to <span class="accent">create a portfolio</span></h2>
<p class="abs center ht-sub">Direct Indexing is like an exchange traded fund (ETF) or index that you customise<br>to suit your investment needs.</p>

<div class="abs step" style="left:24px;top:1468px"><div class="num">1</div><div class="st">Choose your market and<br>how many stocks you want</div><div class="sd">Global, Australian, bond and cash options</div></div>
<div class="abs step" style="left:413px;top:1468px"><div class="num">2</div><div class="st">Choose ethics and themes<br>to screen out</div><div class="sd">Ethically Aligned Investment Options</div></div>
<div class="abs step" style="left:802px;top:1468px"><div class="num">3</div><div class="st">Choose themes to add or<br>tilt your portfolio towards</div><div class="sd">Flexible Portfolio Customization</div></div>

<div class="abs panel" style="left:90px;top:1614px;width:232px;height:340px">
  <div class="pf-head">Passive Direct Indexing Portfolios</div>
  <div class="pf-label">Australian Leaders</div><div class="pf-input" style="width:220px">25%</div>
  <div class="pf-label">Stocks to include in Australian Leaders</div><div class="pf-input" style="width:220px">25</div>
  <div class="pf-label">Global Leaders 15</div><div class="pf-input" style="width:220px">75%</div>
  <div class="pf-label">Stocks to include in Global Leaders</div><div class="pf-input" style="width:220px">15</div>
</div>

<div class="abs panel" style="left:452px;top:1614px;width:294px;height:340px">
  <div class="tile-grid">
    <div class="tile">Climate Change<span class="ic"></span></div><div class="tile">War<span class="ic"></span></div>
    <div class="tile">Human Rights<span class="ic"></span></div><div class="tile">Health<span class="ic"></span></div>
    <div class="tile">Vices<span class="ic"></span></div><div class="tile">Animal Rights<span class="ic"></span></div>
    <div class="tile">Religion<span class="ic"></span></div><div class="tile">Social<span class="ic"></span></div>
  </div>
</div>

<div class="abs panel" style="left:836px;top:1614px;width:302px;height:340px">
  <div style="padding:8px 0 0 10px;font-weight:700;font-size:15px;color:#444">Tilts</div>
  <div class="tile-grid">
    <div class="tile">Investment Style<span>Factors</span></div><div class="tile">Climate Change<span class="ic"></span></div>
    <div class="tile on">Technology<span class="ic"></span></div><div class="tile">Consumption<span class="ic"></span></div>
    <div class="tile">Commodities<span class="ic"></span></div><div class="tile">Health<span class="ic"></span></div>
  </div>
</div>

<h2 class="abs center h-cond seize">Seize Control of Your Investments Today</h2>
<div class="btn seize-btn">Start Now</div>

<h2 class="abs center h-cond t-title">Client <span class="accent">Testimonials</span></h2>
<p class="abs center t-sub">Discover what our satisfied clients have to say about the transformative<br>impact of our direct indexing services.</p>
<div class="abs t-card"></div>
<div class="abs quote" style="left:176px;top:2366px">&rdquo;</div>
<div class="abs quote" style="left:904px;top:2738px;transform:rotate(180deg)">&rdquo;</div>
<div class="abs avatar" role="img" aria-label="Client profile photo"></div>
<div class="abs center t-name">Marcus 36-45 years old</div>
<p class="abs t-text">Parcelfolio offers a great product with outstanding dashboard tools that allow me to drill all the way down into my investment and view each holding. Plus great customer support. Strongly recommended</p>
<div class="abs dots"><i></i><i></i><i></i><i></i></div>

<h2 class="abs center h-cond aw-title">Multi-award <span class="accent">winning portfolios</span></h2>
<div class="abs trophy" role="img" aria-label="Illustration of a gold trophy with a star"></div>
<p class="abs aw-text">Parcelfolio Direct Indexing is leading the way in personalized investment solutions, offering direct ownership of global and Australian shares for tailored portfolios.</p>

<h2 class="abs center h-cond rc-title">Where Innovation <span class="accent">Meets Recognition</span></h2>
<p class="abs center rc-sub">Our dedication to creating bespoke investment solutions has not gone unnoticed.</p>
<div class="abs rc-box"></div>
<div class="abs press" style="top:3604px;height:236px" role="img" aria-label="Newspaper article screenshot: Direct indexing, the next generation ETFs"></div>
<div class="abs press" style="top:3848px;height:274px" role="img" aria-label="Newspaper article screenshot: Tailor-made portfolio trend takes on ETFs"></div>
<div class="abs rc-bar"></div>
<div class="abs rc-h" style="top:3650px">Customized Investments</div>
<p class="abs rc-p" style="top:3694px">The journey of innovation and customization we're on has caught the eye of the financial press, underscoring our efforts to tailor each portfolio to its owner's aspirations.</p>
<div class="abs rc-h" style="top:3834px">Controlled Investment Decisions</div>
<p class="abs rc-p" style="top:3878px">The articles and mentions featured below showcase our commitment to leading the charge in personalized investment. Join us in <u>exploring these highlights</u>.</p>

<div class="abs cta-photo" role="img" aria-label="Black and white photo of a laptop and phone showing investment charts"></div>
<div class="abs cta-panel"></div>
<h2 class="abs h-cond cta-title">Transform Your <span class="accent">Investments<br>Today</span></h2>
<p class="abs cta-text">Start your journey towards a customized investment portfolio that aligns with your values and financial aspirations. <a>Contact us now.</a></p>

<footer>
  <div class="abs f-col" style="left:24px;width:150px"><h4>Solutions</h4><ul><li>– Ethical Investing</li><li>– Superannuation</li><li>– Portfolios</li><li>– Intermediaries</li></ul></div>
  <div class="abs f-col" style="left:214px;width:150px"><h4>Company</h4><ul><li>– About Us</li><li>– FAQs</li><li>– Media</li><li>– Privacy Policy</li><li>– How we use your information</li></ul></div>
  <div class="abs f-col" style="left:428px;width:250px"><h4>Contact Us</h4><ul><li style="line-height:20px">&#9873;&nbsp; Level 3, 120 Harbour Lane Melbourne<br>&nbsp;&nbsp;&nbsp;&nbsp; Victoria 3000</li><li style="margin-top:14px">&#9742;&nbsp; 1300 555 214</li><li style="margin-top:14px">&#9993;&nbsp; contact@kestrelvault.com</li></ul></div>
  <div class="abs f-col" style="left:716px;width:250px"><h4>Latest Insights</h4><ul><li style="line-height:20px">Housing Affordability Update | Kestrel<br>Investment Insights</li><li style="margin-top:14px">Is the stock bubble about to burst?</li><li style="margin-top:14px">RBA rate cuts trigger house price rebound</li></ul></div>
  <div class="abs f-col" style="left:998px;width:150px"><h4>Invest With Us</h4><ul><li>– Member login</li><li>– Leave us a review</li></ul></div>
  <p class="abs f-disc">The information on this site contains general information and does not take into account your personal objectives, financial situation or needs. Past performance is not an indicator of future performance. Kestrel Vault Management (ABN 12 345 678 901) is a Corporate Authorised Representative of Kestrel Advice Pty Ltd - AFSL 500123.<br><u>View our Financial Services Guide.</u></p>
  <div class="btn f-btn" style="left:874px;width:88px">Book for Free</div>
  <div class="btn f-btn" style="left:978px;width:82px">Subscribe</div>
  <div class="btn f-btn" style="left:1076px;width:98px">Get Started</div>
  <div class="abs f-copy">Copyright 2025 © Kestrel Vault</div>
</footer>

</body>
</html>
```